I am a company selling interior designing materials

HI, I am selling interior design materials and require a namecard which is more outstanding while following a certain details placement as attached.

My clients are mainly interior designers so it has to attract their attention rather than feeling that its "just another namecard". I am selling wallcoverings, fabrics, acoustics and carpets.

Target Market(s)

interior designers designing hotels, commerical offices.

Contact Information for Business Card

As per attached.
Please change address to 47 Jalan 16 Tampines #05-02 Velmora Building Singapore 527314

Font styles to use
Other font styles liked:
• calibri

Requirements
Must have
• (1) company logo on top in the middle. Placement of contac details to be the same
• (2) company color is blue/green cymk 75/8/42/0
• (3) "KTV" logo to be prominent
• (4) You may change the logo but there should be a "swirl" surrounding the word KTV like current logo. The swirl pattern does not need to follow current logo and you may propose.
Should not have
• (1) there should not be any designs above "KTV" logo
• (2) no sharp triangles or angles

```html
<!DOCTYPE html>
<html lang="en">
<head>
<meta charset="utf-8">
<title>KTV Business Card</title>
<link href="https://fonts.googleapis.com/css2?family=Open+Sans:wght@400;600&display=swap" rel="stylesheet">
<style>
  :root {
    --teal: #40b5a6;
    --teal-dark: #2fa597;
    --red: #e8323c;
    --ink: #555555;
    --ink-soft: #6a6a6a;
    --paper: #fbfbfb;
    --backdrop: #2b2b2b;
    --silver: #d9dcdc;
  }
  * { margin: 0; padding: 0; box-sizing: border-box; }
  html, body {
    width: 1200px; height: 960px; overflow: hidden;
    background: var(--backdrop);
    font-family: "Open Sans", Arial, sans-serif;
  }
  .stage {
    position: relative; width: 1200px; height: 960px;
  }
  .card {
    position: absolute; left: 300px;
    width: 600px; height: 343px;
    border-radius: 2px;
    overflow: hidden;
  }
  /* Back side */
  .card-back { top: 90px; background: var(--teal); }
  .back-brand {
    position: absolute; inset: 0;
    display: flex; flex-direction: column; align-items: center; justify-content: center;
    gap: 18px;
  }
  .back-mark {
    display: flex; align-items: center; gap: 16px;
  }
  .back-dot {
    width: 28px; height: 28px; border-radius: 50%; background: var(--silver);
  }
  .back-name {
    font-size: 88px; font-weight: 600; color: var(--silver);
    letter-spacing: 2px; line-height: 1;
  }
  .back-company {
    font-size: 14px; color: #ffffff; letter-spacing: 1px;
  }
  .back-company .lead { color: var(--red); }

  /* Front side */
  .card-front { top: 500px; background: var(--paper); }
  .front-layout {
    position: absolute; inset: 0;
    display: flex; align-items: center;
    padding: 0 44px 0 40px;
  }
  .front-brand {
    width: 250px;
    display: flex; flex-direction: column; align-items: center; gap: 10px;
  }
  .front-mark { display: flex; align-items: center; gap: 12px; }
  .front-dot { width: 18px; height: 18px; border-radius: 50%; background: var(--teal); }
  .front-name {
    font-size: 50px; font-weight: 600; color: var(--ink); letter-spacing: 1px; line-height: 1;
  }
  .front-company { font-size: 12px; color: var(--ink); white-space: nowrap; }

  .contact { margin-left: 34px; }
  .contact-head {
    border-left: 2px solid #777; padding-left: 14px;
  }
  .person { font-size: 24px; font-weight: 600; letter-spacing: 0.5px; line-height: 1.15; }
  .person .given { color: var(--teal-dark); }
  .person .family { color: var(--red); }
  .address { font-size: 13px; color: var(--ink); letter-spacing: 0.6px; line-height: 1.5; margin-top: 2px; }

  .contact-lines {
    border-left: 2px solid var(--red);
    margin-top: 10px; padding-left: 14px;
  }
  .line {
    display: flex; align-items: center; gap: 12px;
    font-size: 13px; color: var(--ink-soft); letter-spacing: 0.6px; line-height: 1.6;
  }
  .line svg { width: 16px; height: 12px; flex: none; }
</style>
</head>
<body>
<main class="stage">

  <section class="card card-back" aria-label="Card back">
    <div class="back-brand">
      <div class="back-mark">
        <span class="back-dot"></span>
        <span class="back-name">KTV</span>
      </div>
      <p class="back-company"><span class="lead">KelTavio</span> Interior Furnishings Pte Ltd</p>
    </div>
  </section>

  <section class="card card-front" aria-label="Card front">
    <div class="front-layout">
      <div class="front-brand">
        <div class="front-mark">
          <span class="front-dot"></span>
          <span class="front-name">KTV</span>
        </div>
        <p class="front-company">KelTavio Interior Furnishings Pte Ltd</p>
      </div>

      <div class="contact">
        <div class="contact-head">
          <h1 class="person"><span class="given">LYDIA</span> <span class="family">TAN</span></h1>
          <p class="address">47 Jalan 16 Tampines #05-02<br>Velmora Building Singapore 527314</p>
        </div>
        <div class="contact-lines">
          <p class="line">
            <svg viewBox="0 0 16 12" aria-hidden="true"><path d="M1 4c2-3 12-3 14 0l-1 2-3-1V4H5v1L2 6z M4 7h8l2 4H2z" fill="var(--teal)"/></svg>
            (65) 8127 4630
          </p>
          <p class="line">
            <svg viewBox="0 0 16 12" aria-hidden="true"><rect x="1" y="1" width="14" height="10" fill="none" stroke="var(--teal)" stroke-width="1.4"/><path d="M1 1l7 6 7-6" fill="none" stroke="var(--teal)" stroke-width="1.4"/></svg>
            lydia@ktvfurnishings.com
          </p>
        </div>
      </div>
    </div>
  </section>

</main>
</body>
</html>
```